Business card design for holistic health care clinic

We need a double-sided business card design for our holistic health care clinic that integrates our logo design and also its color scheme. My business is called Veralune. It is an integrative medicine clinic. You have already done the logo for me. Please ensure an elegant and upscale design that is not cluttered, but still has all the necessary information (please see below for details).

Target Market(s)

Wellness, fitness, rehabilitation for educated, well-traveled open-minded clients who are focused on natural, organic, balanced and preventive healthcare and lifestyle.

Industry/Entity Type

Medical

Contact Information for Business Card

Modern, clean.

Number of Pages Required

1 page

Font styles to use
Serif
Sans Serif

Colors

Designer to choose colors to be used in the design.

Requirements
Must have
• Logo on one side, all other information on the other side.
• Other information should include:
• Tobias Wendmere - DOE, CPT, LMT
• 1450 North Calloway Street
• Austin, TX 78744
• 512 555 0184
• 818 555 0127
• info@VeraluneHealth.com
• t.wendmere@VeraluneHealth.com
Nice to have
• Darker background on front - but not totally black - shaded/dark gray.

```html
<!DOCTYPE html>
<html lang="en">
<head>
<meta charset="utf-8">
<title>Veralune Business Card</title>
<link href="https://fonts.googleapis.com/css2?family=Montserrat:wght@400;600;700&display=swap" rel="stylesheet">
<style>
  :root {
    --backdrop: #3a3430;
    --card: #141414;
    --card-edge: #1d1d1d;
    --brand-blue: #1a8fd6;
    --silver: #d9d9d9;
    --text-grey: #bdbdbd;
    --divider: #3a3a3a;
  }
  * { margin: 0; padding: 0; box-sizing: border-box; }
  html, body {
    width: 1200px; height: 844px; overflow: hidden;
    background: var(--backdrop);
    font-family: "Montserrat", Arial, sans-serif;
  }
  .stage { position: relative; width: 1200px; height: 844px; }
  .card {
    position: absolute; top: 279px;
    width: 500px; height: 286px;
    background: var(--card);
    border: 1px solid var(--card-edge);
    box-shadow: 0 10px 30px rgba(0,0,0,.45);
  }
  .card--contact { left: 75px; }
  .card--brand { left: 625px; display: flex; align-items: center; justify-content: center; }

  .brand-name { font-weight: 700; letter-spacing: 1px; text-transform: uppercase; line-height: 1; }
  .card--contact .brand-name {
    position: absolute; left: 32px; top: 166px;
    font-size: 36px; color: var(--brand-blue);
  }
  .card--brand .brand-name { font-size: 52px; color: var(--silver); }

  .divider {
    position: absolute; left: 262px; top: 28px;
    width: 1px; height: 230px; background: var(--divider);
  }
  .details { position: absolute; left: 280px; top: 40px; right: 12px; color: var(--text-grey); font-size: 11.5px; }
  .person { display: flex; align-items: baseline; gap: 6px; flex-wrap: wrap; margin-bottom: 10px; }
  .person-name { color: var(--brand-blue); font-weight: 700; font-size: 14px; text-transform: uppercase; }
  .person-credentials { font-size: 10.5px; color: var(--text-grey); }
  .address { line-height: 1.45; margin-bottom: 8px; }
  .contact-list { list-style: none; }
  .contact-list li { display: flex; align-items: center; gap: 8px; line-height: 1.6; }
  .contact-list svg { width: 11px; height: 11px; fill: var(--brand-blue); flex: none; }
</style>
</head>
<body>
<main class="stage">
  <section class="card card--contact">
    <div class="brand-name">Veralune</div>
    <div class="divider"></div>
    <div class="details">
      <div class="person">
        <span class="person-name">Tobias Wendmere</span>
        <span class="person-credentials">DOE, CPT, LMT</span>
      </div>
      <p class="address">1450 North Calloway Street<br>Austin, TX 78744</p>
      <ul class="contact-list">
        <li><svg viewBox="0 0 12 12"><path d="M1 4c0-2 2-3 5-3s5 1 5 3H8.5V3h-5v1H1zm2 1h6l2 5H1l2-5zm3 1.5a1.5 1.5 0 100 3 1.5 1.5 0 000-3z"/></svg>512 555 0184</li>
        <li><svg viewBox="0 0 12 12"><path d="M3.5 0h5a1 1 0 011 1v10a1 1 0 01-1 1h-5a1 1 0 01-1-1V1a1 1 0 011-1zm.5 1.5v8h4v-8H4zm2 8.7a.6.6 0 100 1.2.6.6 0 000-1.2z"/></svg>818 555 0127</li>
        <li><svg viewBox="0 0 12 12"><path d="M0 2h12v8H0V2zm1 1v.4l5 3.2 5-3.2V3H1zm0 1.6V9h10V4.6L6 7.8 1 4.6z"/></svg>info@VeraluneHealth.com</li>
        <li><svg viewBox="0 0 12 12"><path d="M0 2h12v8H0V2zm1 1v.4l5 3.2 5-3.2V3H1zm0 1.6V9h10V4.6L6 7.8 1 4.6z"/></svg>t.wendmere@VeraluneHealth.com</li>
        <li><svg viewBox="0 0 12 12"><circle cx="6" cy="6" r="5.5"/></svg>www.VeraluneHealth.com</li>
      </ul>
    </div>
  </section>

  <section class="card card--brand">
    <div class="brand-name">Veralune</div>
  </section>
</main>
</body>
</html>
```